Business Card Design Project

We currently have existing logo. Looking to have nice colorful business cards done.
We would like the name of business, phone, address, email and website

Target Market(s)

25-50

Industry/Entity Type

Business

Requirements
Must have
• We are currently using
Samrakan font for our business name
Rage italic font for tag line..
you may visit our website at www.velmorista.com to get good feel

velmorista means colors in India. google velmorista to get more info

```html
<!DOCTYPE html>
<html lang="en">
<head>
<meta charset="utf-8">
<title>Velmorista India Restaurant – Business Card</title>
<link rel="stylesheet" href="https://fonts.googleapis.com/css2?family=Cabin:wght@400;500&family=Italianno&display=swap">
<style>
  :root {
    --paper: #ffffff;
    --brand-brown: #6b3410;
    --ink: #141414;
    --icon-red: #7a2a2a;
    --rule-dark: #3a0a0c;
    --band-red: #a52a35;
    --band-gold: #d9823a;
  }
  html, body {
    margin: 0;
    padding: 0;
    overflow: hidden;
    background: var(--paper);
  }
  .card {
    position: relative;
    width: 1200px;
    height: 800px;
    background: var(--paper);
    overflow: hidden;
    font-family: "Cabin", "Candara", sans-serif;
    color: var(--ink);
  }
  .brand-dot {
    position: absolute;
    left: 12px;
    top: 8px;
    width: 94px;
    height: 94px;
    border-radius: 50%;
    background: var(--band-red);
  }
  .brand-name {
    position: absolute;
    left: 20px;
    top: 118px;
    margin: 0;
    font-family: "Cabin", "Candara", sans-serif;
    font-weight: 500;
    font-size: 96px;
    line-height: 1;
    letter-spacing: 2px;
    color: var(--brand-brown);
  }
  .tagline {
    position: absolute;
    left: 258px;
    top: 250px;
    margin: 0;
    font-family: "Italianno", cursive;
    font-size: 60px;
    line-height: 1;
    letter-spacing: 9px;
    color: var(--ink);
  }
  .phone {
    position: absolute;
    right: 20px;
    top: 26px;
    display: flex;
    align-items: center;
    gap: 14px;
    font-size: 32px;
    letter-spacing: 5px;
    font-weight: 500;
  }
  .phone-icon {
    width: 50px;
    height: 40px;
  }
  .contact {
    position: absolute;
    right: 20px;
    top: 410px;
    margin: 0;
    font-style: normal;
    text-align: right;
    font-size: 32px;
    line-height: 42.5px;
    letter-spacing: 4.5px;
    font-weight: 500;
  }
  .contact span { display: block; }
  .band-rule {
    position: absolute;
    left: 0;
    top: 645px;
    width: 100%;
    height: 7px;
    background: var(--rule-dark);
  }
  .band {
    position: absolute;
    left: 0;
    top: 652px;
    width: 100%;
    height: 148px;
    background: linear-gradient(180deg, var(--band-red) 0%, #a8303a 45%, #b04436 100%);
  }
</style>
</head>
<body>
  <main class="card">
    <span class="brand-dot" aria-hidden="true"></span>
    <h1 class="brand-name">velmorista</h1>
    <p class="tagline">India Restaurant</p>

    <div class="phone">
      <svg class="phone-icon" viewBox="0 0 50 40" aria-hidden="true" fill="none" stroke="var(--icon-red)" stroke-width="2.5" stroke-linejoin="round">
        <path d="M4 14 C4 5 46 5 46 14 L46 17 L36 17 L36 12 L14 12 L14 17 L4 17 Z"/>
        <path d="M12 18 L38 18 L44 36 L6 36 Z"/>
        <g fill="var(--icon-red)" stroke="none">
          <rect x="18" y="22" width="3" height="3"/><rect x="24" y="22" width="3" height="3"/><rect x="30" y="22" width="3" height="3"/>
          <rect x="17" y="27" width="3" height="3"/><rect x="24" y="27" width="3" height="3"/><rect x="31" y="27" width="3" height="3"/>
        </g>
      </svg>
      <span class="phone-number">408.555.0147</span>
    </div>

    <address class="contact">
      <span class="street">1820 Larkspur Avenue</span>
      <span class="city">Alder Grove, CA</span>
      <span class="zip">95180</span>
      <span class="email">info@velmorista.com</span>
      <span class="web">www.velmorista.com</span>
    </address>

    <div class="band-rule" aria-hidden="true"></div>
    <div class="band" role="img" aria-label="Decorative band of golden orange scrollwork swirls on deep red"></div>
  </main>
</body>
</html>
```